Design a DL flyer double sided 4 colour 210mm x 95 mm (portrait) for the launch of a new yoga studio opening in North Melbourne on the 23 November 2013.
The final design should communicate with a strong call to action- the opening date , register to receive your first class free and like us on Chatterbox.
The studio provides a tranquil, open space to practice yoga, create a feeling of light, peace and a nurturing environment, please create this feeling in the design.

An example design mock (rough design feel free to move around as required, includes final content) print specifications, logo, typography style and image attached.
The reverse side to include logo, address and please design the timetable for the launch week (refer design mock)
Have also attached a reverse logo for a dark background and are open to designer providing examples with various background colours and effects.
Back content can be moved to the front side if required to facilitate design

Target Market(s)

People in the area who are practicing yoga elsewhere and encourage them to come to the studio to try us out with a free opening offer in our first week. And people new to yoga wanting to give it a try.
Experienced yoga people and people new to yoga - all ages

Industry/Entity Type

Environment

Requirements
Must have
• The Lotus Nook logo physical address, website address, the tagline live, breathe, love...
The final design should communicate with a strong call to action- the opening date , register to receive your first class free and like us on Chatterbox. and the website address thelotusnook.com.au, drive them to the website to register.
The studio provides a tranquil, open space to practice yoga, create a feeling of light, peace and a nurturing environment, please create this feeling in the design

```html
<!DOCTYPE html>
<html lang="en">
<head>
<meta charset="utf-8">
<title>The Lotus Nook – Opening Flyer</title>
<link href="https://fonts.googleapis.com/css2?family=Open+Sans:wght@400;600&family=Crimson+Text:ital@1&display=swap" rel="stylesheet">
<style>
  :root{
    --bg:#c9c9c9;
    --green-deep:#1f3311;
    --green-dark:#2a4417;
    --green-mid:#3c5e22;
    --green-light:#5d8636;
    --gold:#d8c65a;
    --yellow:#f2ef2e;
    --orange:#f0901e;
    --white:#ffffff;
    --map-bg:#ebe6dc;
  }
  *{box-sizing:border-box;margin:0;padding:0}
  html,body{width:1200px;height:1200px;overflow:hidden}
  body{background:var(--bg);font-family:"Open Sans",Arial,sans-serif;color:var(--white);position:relative}
  .panel{position:absolute;top:48px;width:505px;height:1078px;overflow:hidden;
    background:linear-gradient(180deg,var(--green-mid) 0%,var(--green-dark) 55%,var(--green-deep) 100%)}
  .panel--front{left:85px}
  .panel--back{left:610px}
  .abs{position:absolute;left:0;right:0;text-align:center}
  .rule{position:absolute;left:0;right:0;height:2px;background:var(--gold)}

  /* front */
  .front-header{top:0;height:120px;background:linear-gradient(180deg,var(--green-deep),var(--green-dark))}
  .front-header .headline{position:absolute;left:0;right:0;top:22px;text-align:center;font-size:24px;font-weight:600;color:var(--yellow)}
  .front-header .subline{position:absolute;left:0;right:0;top:56px;text-align:center;font-size:22px}
  .hero-photo{position:absolute;left:0;right:0;top:120px;height:460px;
    background:radial-gradient(ellipse at 50% 40%,#e7ece0 0%,#8fb06a 30%,#3f6624 65%,#22380f 100%)}
  .brand{position:absolute;left:0;right:0;display:flex;align-items:center;justify-content:center;gap:12px}
  .brand__dot{width:34px;height:34px;border-radius:50%;background:var(--orange)}
  .brand__name{font-size:40px;font-weight:600;color:var(--orange);letter-spacing:-.5px}
  .tagline{position:absolute;left:0;right:0;text-align:center;font-size:17px}
  .front-brand{top:478px}
  .front-tagline{top:528px;left:-60px}
  .opening-title{top:648px;font-size:32px;color:var(--orange)}
  .opening-dates{top:688px;font-size:28px}
  .booking{top:778px;font-size:20px;line-height:28px}
  .booking .free{color:var(--yellow)}
  .social{top:848px;display:flex;justify-content:center;align-items:center;gap:10px;font-size:20px;line-height:26px}
  .social__mark{width:34px;height:34px;background:#3b5b9a;border-radius:4px}
  .social__name{font-size:28px;font-weight:600;color:var(--white)}
  .social__page{text-align:left}
  .friends{top:910px;font-size:20px}
  .specials{top:996px;font-size:18px;color:var(--yellow)}
  .front-url{top:1040px;font-size:18px}

  /* back */
  .back-header{position:absolute;left:0;right:0;top:0;height:138px;background:linear-gradient(180deg,var(--green-deep),var(--green-dark))}
  .back-brand{top:54px}
  .back-tagline{top:103px;left:-60px;font-size:17px}
  .about{top:190px;padding:0 40px;font-family:"Crimson Text",Georgia,serif;font-style:italic;font-size:18px;line-height:20.5px}
  .schedule-title{top:426px;font-size:18px}
  .schedule-sub{top:450px;font-size:13px}
  .timetable{position:absolute;left:0;right:0;top:474px;height:152px;display:grid;grid-template-columns:repeat(7,1fr);
    border-top:2px solid var(--gold);border-bottom:2px solid var(--gold)}
  .day{border-left:1px solid var(--gold);text-align:center;font-size:13.5px}
  .day:first-child{border-left:none}
  .day__name{margin-top:10px;height:34px}
  .day__times{line-height:19.5px}
  .location{top:642px;font-size:17px}
  .map{position:absolute;left:21px;width:463px;top:670px;height:286px;border:2px solid var(--gold);
    background:linear-gradient(135deg,var(--map-bg),#d8d2c4)}
  .contact{top:976px;font-size:16px;line-height:21.5px}
  .contact__social{display:inline-flex;align-items:center;gap:6px}
  .contact__mark{width:16px;height:16px;background:#3b5b9a;border-radius:2px}
</style>
</head>
<body>

<section class="panel panel--front">
  <header class="abs front-header">
    <p class="headline">New Yoga Studio opening 23 November</p>
    <p class="subline">First class FREE in opening week!</p>
  </header>
  <div class="rule" style="top:118px"></div>
  <div class="hero-photo" role="img" aria-label="Woman meditating cross-legged beside water in a lush green rainforest"></div>
  <div class="brand front-brand"><span class="brand__dot"></span><span class="brand__name">The Lotus Nook</span></div>
  <p class="tagline front-tagline">live, breathe, love...</p>
  <div class="rule" style="top:580px"></div>

  <p class="abs opening-title">OPENING WEEK</p>
  <p class="abs opening-dates">23 Nov – 29 Nov inclusive</p>
  <p class="abs booking">To book your <span class="free">FREE</span> class<br>go online to register and book,</p>
  <div class="abs social">
    <span class="social__mark"></span><span class="social__name">Chatterbox</span>
    <span class="social__page">The Lotus Nook<br>Melbourne</span>
  </div>
  <p class="abs friends">and tell your friends!</p>
  <p class="abs specials">View other opening specials at:</p>
  <div class="rule" style="top:1026px"></div>
  <p class="abs front-url">WWW.THELOTUSNOOK.COM.AU</p>
</section>

<section class="panel panel--back">
  <header class="back-header"></header>
  <div class="brand back-brand"><span class="brand__dot"></span><span class="brand__name">The Lotus Nook</span></div>
  <p class="tagline back-tagline">live, breathe, love...</p>
  <div class="rule" style="top:138px"></div>
  <div class="rule" style="top:154px;height:1px"></div>

  <p class="abs about">A generously sized natural studio in North Melbourne, providing dynamic flow vinyasa and restorative yoga for all levels from newbies to experienced, with a collection of the best teachers.<br>Embark on a journey to happiness within yourself<br>– be healthy in your body and mind. –<br>Science is finally proving what yogis have<br>known all along.... yoga is good for you!<br>A tranquil space to de stress, build strength and healing in our bodies through our own tapas (internal heat).</p>

  <div class="rule" style="top:416px"></div>
  <p class="abs schedule-title">OPEN SEVEN DAYS</p>
  <p class="abs schedule-sub">See TIMETABLE for Class Times</p>
  <div class="timetable">
    <div class="day"><p class="day__name">Sat</p><p class="day__times">9.00 AM<br>10.30 AM<br>4.00 PM</p></div>
    <div class="day"><p class="day__name">Sun</p><p class="day__times">9.00 AM<br>10.30 AM<br>4.00 PM</p></div>
    <div class="day"><p class="day__name">Mon</p><p class="day__times">6.30 AM<br>9.30 AM<br>12.30 PM<br>5.30 PM<br>7.00 PM</p></div>
    <div class="day"><p class="day__name">Tue</p><p class="day__times">6.30 AM<br>9.30 AM<br>12.30 PM<br>5.30 PM<br>7.00 PM</p></div>
    <div class="day"><p class="day__name">Wed</p><p class="day__times">6.30 AM<br>9.30 AM<br>12.30 PM<br>5.30 PM<br>7.00 PM</p></div>
    <div class="day"><p class="day__name">Thu</p><p class="day__times">6.30 AM<br>9.30 AM<br>12.30 PM<br>5.30 PM<br>7.00 PM</p></div>
    <div class="day"><p class="day__name">Fri</p><p class="day__times">6.30 AM<br>9.30 AM<br>12.30 PM<br>5.30 PM<br>7.00 PM</p></div>
  </div>

  <p class="abs location">Find us at 58 Arden Lane, North Melbourne VIC 3003</p>
  <div class="map" role="img" aria-label="Street map of North Melbourne showing the studio location"></div>
  <div class="rule" style="top:968px"></div>
  <p class="abs contact">Phone: 0400-555018<br>Email: hello@thelotusnook.com.au<br><span class="contact__social"><span class="contact__mark"></span>chatterbox.com/thelotusnookmelbourne</span><br>WWW.THELOTUSNOOK.COM.AU</p>
</section>

</body>
</html>
```